Modern Business Card for Lanternfield 2018

Our company assumes the best about people. We are creating an online community of entrepreneurs and business leaders who struggle with marketing their business online.

This business card should POP! We recently got a new logo and are launching a new website next month, so our business cards should make a statement that feels:
-Fresh
-Smart
-Trustworthy
-Fun

Target Market(s)

small business owners, entrepreneurs

Industry/Entity Type

Digital Marketing

Contact Information for Business Card

Dimensions: 3.5" x 2"

Font styles to use
Sans Serif

Colors
f37122
ffffff

Requirements
Must have
• We need a business card with a modern, bold design. We will use one side of the card as a lead-generation offer, so text on one side will need to fit up to 140 characters. The business card should stick to our core colors (orange, black, and white).
Nice to have
• We think a vertical "portrait" design could be interesting.
Should not have
• Should not look like a traditional business card. The round icon should stand out from a distance.

```html
<!DOCTYPE html>
<html lang="en">
<head>
<meta charset="utf-8">
<title>Lanternfield Business Card</title>
<link href="https://fonts.googleapis.com/css2?family=Montserrat:wght@400;600;800&family=Roboto+Condensed:wght@400&display=swap" rel="stylesheet">
<style>
  :root {
    --orange: #f37122;
    --white: #ffffff;
    --card-dark: #2e2d30;
    --ink: #1f1f1f;
    --stage: #262626;
    --faint: #f1f1f3;
  }
  html, body { margin: 0; padding: 0; overflow: hidden; }
  body {
    width: 1200px; height: 1200px;
    background: var(--stage);
    display: flex; align-items: center; justify-content: center; gap: 60px;
    font-family: "Montserrat", sans-serif;
  }
  .card {
    position: relative;
    width: 400px; height: 700px;
    overflow: hidden;
    box-shadow: 0 20px 50px rgba(0,0,0,0.45);
  }
  .card-back { background: var(--card-dark); color: var(--white); }
  .card-front { background: var(--white); color: var(--ink); }
  .mark-dot {
    position: absolute; left: 50%; top: 62px;
    width: 50px; height: 50px; margin-left: -25px;
    border-radius: 50%; background: var(--orange);
  }
  .brand-name {
    position: absolute; top: 138px; left: 0; right: 0;
    text-align: center; font-weight: 800; font-size: 40px; letter-spacing: 1px;
    margin: 0;
  }
  .brand-tagline {
    position: absolute; top: 192px; left: 0; right: 0;
    text-align: center; font-size: 12px; font-weight: 600;
    letter-spacing: 1.5px; text-transform: uppercase; margin: 0;
  }
  .promise {
    position: absolute; top: 272px; left: 0; right: 0;
    text-align: center; color: var(--orange);
    font-weight: 600; font-size: 22px; line-height: 30px; letter-spacing: 1.5px;
    margin: 0; text-transform: uppercase;
  }
  .accent-circle {
    position: absolute; left: -110px; bottom: -80px;
    width: 250px; height: 250px; border-radius: 50%;
    background: var(--orange);
  }
  .offer {
    position: absolute; left: 160px; bottom: 30px; width: 230px;
    font-family: "Roboto Condensed", sans-serif; font-size: 18px; line-height: 23px;
    margin: 0;
  }
  .offer-link { color: var(--orange); display: block; }
  .person-name {
    position: absolute; top: 290px; left: 0; right: 0;
    text-align: center; font-size: 36px; margin: 0; letter-spacing: -0.5px;
  }
  .person-name .first { font-weight: 800; }
  .person-name .last { font-weight: 400; }
  .person-title {
    position: absolute; top: 342px; left: 0; right: 0;
    text-align: center; color: var(--orange);
    font-size: 16px; font-weight: 600; letter-spacing: 1.5px; margin: 0;
  }
  .faint-circle {
    position: absolute; right: -90px; bottom: 60px;
    width: 280px; height: 280px; border-radius: 50%;
    background: var(--faint);
  }
  .email {
    position: absolute; bottom: 42px; left: 0; right: 0;
    text-align: center; font-size: 16px; font-weight: 600; letter-spacing: 1px; margin: 0;
  }
</style>
</head>
<body>
  <section class="card card-back">
    <div class="mark-dot"></div>
    <h1 class="brand-name">LANTERNFIELD</h1>
    <p class="brand-tagline">Tell stories that inspire action</p>
    <p class="promise">Reach more people.<br>Make more money.<br>Create more impact.</p>
    <div class="accent-circle"></div>
    <p class="offer">Get Your Free Lanternfield Starter Package and Our Marketing Guide Today at <span class="offer-link">lanternfieldhq.com/start</span></p>
  </section>
  <section class="card card-front">
    <div class="mark-dot"></div>
    <h2 class="person-name"><span class="first">DANA</span> <span class="last">WHITMORE</span></h2>
    <p class="person-title">STORY MARKETING COACH</p>
    <div class="faint-circle"></div>
    <p class="email">DANA@LANTERNFIELDHQ.COM</p>
  </section>
</body>
</html>
```